Funeral Services Site

We need a website for a Funeral Services company. The old website is: www.rouwcentrumkorvelaer.be We need the same structure and text.

Target Market(s)

Customers.

Coding

Coded - Design and coding required

Number of Pages Required

4 page

Font styles to use
Serif
Sans Serif
Script

```html
<!DOCTYPE html>
<html lang="en">
<head>
<meta charset="utf-8">
<title>Funeral home Korvelaer bvba – Contact</title>
<link href="https://fonts.googleapis.com/css2?family=Libre+Baskerville:wght@400;700&family=Great+Vibes&family=Jost:wght@400;500&display=swap" rel="stylesheet">
<style>
:root{
  --gold:#a87d05;
  --dark:#333333;
  --ink:#111111;
  --text:#2b2b2b;
  --light:#f2f2f2;
  --frame:#cfcfcf;
  --white:#ffffff;
  --map:#efefef;
}
*{margin:0;padding:0;box-sizing:border-box}
html,body{width:1003px;height:1200px;overflow:hidden;background:var(--white)}
body{position:relative;font-family:'Jost',sans-serif;color:var(--text)}
.topbar{position:absolute;left:0;top:0;width:1003px;height:35px;background:var(--dark);color:var(--white)}
.topbar .item{position:absolute;top:9px;display:flex;align-items:center;gap:6px}
.topbar .phone{left:118px;font-size:13px}
.topbar .mail{left:240px;font-size:11px}
.lang{position:absolute;right:118px;top:4px;width:48px;height:27px;background:var(--white);color:var(--gold);font-size:11px;display:flex;align-items:center;justify-content:center;gap:3px}
.header{position:absolute;left:0;top:35px;width:1003px;height:85px;background:var(--white)}
.brand{position:absolute;left:118px;top:20px;display:flex;align-items:center;gap:8px}
.brand .dot{width:46px;height:46px;border-radius:50%;background:var(--ink)}
.brand .name{font-family:'Libre Baskerville',serif;font-weight:700;font-size:17px;line-height:20px;color:var(--ink)}
.nav{position:absolute;right:118px;top:0;height:85px;display:flex}
.nav a{display:flex;align-items:flex-start;padding:46px 18px 0;font-family:'Libre Baskerville',serif;font-weight:700;font-size:11px;color:var(--ink);text-decoration:none}
.nav a.active{background:var(--light);color:var(--gold);border-bottom:2px solid var(--gold);padding:45px 13px 0}
.hero{position:absolute;left:0;top:120px;width:1003px;height:321px;
  background:
    radial-gradient(ellipse 140px 160px at 900px 90px,rgba(240,240,200,.95),rgba(240,240,200,0) 100%),
    radial-gradient(ellipse 150px 110px at 700px 270px,rgba(235,235,205,.9),rgba(235,235,205,0) 100%),
    radial-gradient(ellipse 120px 90px at 640px 60px,rgba(110,150,40,.7),rgba(110,150,40,0) 100%),
    linear-gradient(90deg,#0b0b0b 0%,#2a2a28 30%,#4a4a42 45%,#5e7a2c 62%,#8da84a 78%,#c8d39a 100%)}
.hero h1{position:absolute;left:118px;top:62px;font-family:'Great Vibes',cursive;font-weight:400;font-size:50px;line-height:57px;color:var(--white)}
.hero .cta{position:absolute;left:119px;top:202px;width:145px;height:38px;border:2px solid var(--white);color:var(--white);font-family:'Libre Baskerville',serif;font-weight:700;font-size:12px;display:flex;align-items:center;justify-content:center}
.intro{position:absolute;left:0;top:506px;width:1003px;text-align:center;font-family:'Libre Baskerville',serif;font-weight:700;font-size:14.6px;line-height:25px;color:var(--ink)}
.contacts{position:absolute;top:579px;left:210px;display:flex;gap:28px}
.contact{display:flex;gap:11px;align-items:center}
.contact .ic{width:30px;height:30px;border-radius:50%;background:var(--gold);display:flex;align-items:center;justify-content:center}
.contact .lbl{font-size:11.5px;color:var(--ink);line-height:16px}
.contact .val{font-size:10.5px;line-height:16px}
.map{position:absolute;left:118px;top:637px;width:767px;height:260px;border:3px solid var(--frame);
  background:
    radial-gradient(ellipse 60px 70px at 770px 60px,rgba(170,225,160,.8),rgba(170,225,160,0) 100%),
    radial-gradient(ellipse 260px 160px at 380px 120px,#f5f5f5,rgba(245,245,245,0) 100%),
    linear-gradient(160deg,#f0f0f0 0%,#ececec 55%,#e9e9e9 100%)}
.foot-h{position:absolute;top:998px;font-family:'Libre Baskerville',serif;font-weight:700;font-size:11px;color:var(--ink)}
.links{position:absolute;left:119px;top:1018px;list-style:none;font-size:10px;line-height:21.2px}
.links li::before{content:"»";font-size:8px;margin-right:8px}
.details{position:absolute;left:259px;top:1018px;font-size:10px;line-height:15px}
.details .row{display:flex;gap:7px;align-items:flex-start;margin-bottom:8px}
.minimap{position:absolute;left:498px;top:1021px;width:172px;height:92px;background:
  radial-gradient(ellipse 30px 60px at 125px 50px,rgba(150,190,225,.8),rgba(150,190,225,0) 100%),
  linear-gradient(135deg,#e8e8e6,#dedbd6 60%,#d3dfe4)}
.f-brand{position:absolute;left:723px;top:1025px;display:flex;align-items:center;gap:6px}
.f-brand .dot{width:42px;height:42px;border-radius:50%;background:var(--ink)}
.f-brand .name{font-family:'Libre Baskerville',serif;font-weight:700;font-size:15px;line-height:16px;color:var(--ink)}
.social{position:absolute;left:757px;top:1073px;display:flex;gap:7px}
.social span{width:19px;height:17px;display:block}
.bottom{position:absolute;left:0;top:1165px;width:1003px;height:35px;background:#ebebeb;font-size:10.5px;color:var(--text)}
.bottom .copy{position:absolute;left:119px;top:10px}
.bottom .legal{position:absolute;right:117px;top:10px}
</style>
</head>
<body>
<div class="topbar">
  <div class="item phone">
    <svg width="16" height="16" viewBox="0 0 24 24" fill="none" stroke="#fff" stroke-width="1.5"><path d="M5 3l4 1 1 5-2 2c1 3 3 5 6 6l2-2 5 1 1 4-3 2C10 22 2 14 3 6z"/></svg>
    012 34 56 78
  </div>
  <div class="item mail">
    <svg width="16" height="14" viewBox="0 0 24 20" fill="none" stroke="#fff" stroke-width="1.5"><path d="M2 8l10-6 10 6v11H2z M2 8l10 7 10-7"/></svg>
    mourningcenter.korvelaer@example.com
  </div>
  <div class="lang">EN <svg width="7" height="4"><path d="M0 0h7L3.5 4z" fill="#a87d05"/></svg></div>
</div>

<header class="header">
  <div class="brand"><span class="dot"></span><span class="name">Funeral home<br>Korvelaer bvba</span></div>
  <nav class="nav">
    <a>Home</a><a>About us</a><a>Condole online</a><a>Order flowers</a><a class="active">Contact</a>
  </nav>
</header>

<section class="hero" role="img" aria-label="Photograph of white roses and green buds beside a dark piano">
  <h1>A Personal Service In<br>Farewell Guidance</h1>
  <div class="cta">Contact Us Today</div>
</section>

<p class="intro">If you want more information about our services, we are happy to help.<br>Do not hesitate to contact us with all your questions.</p>

<div class="contacts">
  <div class="contact">
    <span class="ic"><svg width="12" height="14" viewBox="0 0 12 16"><path d="M6 0a6 6 0 0 1 6 6c0 4-6 10-6 10S0 10 0 6a6 6 0 0 1 6-6z" fill="#fff"/><circle cx="6" cy="6" r="2" fill="#a87d05"/></svg></span>
    <div><div class="lbl">Address</div><div class="val">Lindeweg 14, 3770 Zussen (Riemst)</div></div>
  </div>
  <div class="contact">
    <span class="ic"><svg width="13" height="13" viewBox="0 0 24 24"><path d="M5 3l4 1 1 5-2 2c1 3 3 5 6 6l2-2 5 1 1 4-3 2C10 22 2 14 3 6z" fill="#fff"/></svg></span>
    <div><div class="lbl">PHONE</div><div class="val">012 34 56 78</div></div>
  </div>
  <div class="contact">
    <span class="ic"><svg width="14" height="12" viewBox="0 0 24 20" fill="none" stroke="#fff" stroke-width="2"><path d="M2 8l10-6 10 6v11H2z M2 8l10 7 10-7"/></svg></span>
    <div><div class="lbl">EMAIL</div><div class="val">mourningcenter.korvelaer@example.com</div></div>
  </div>
</div>

<div class="map" role="img" aria-label="Street map of Zussen with a marker at the funeral home on Lindeweg"></div>

<h3 class="foot-h" style="left:119px">Quick Links</h3>
<h3 class="foot-h" style="left:259px">Contact Details</h3>
<h3 class="foot-h" style="left:498px">Location Map</h3>

<ul class="links">
  <li>Home</li><li>About us</li><li>Condole online</li><li>Order flowers</li><li>Contact</li>
</ul>

<div class="details">
  <div class="row"><svg width="9" height="12" viewBox="0 0 12 16"><path d="M6 0a6 6 0 0 1 6 6c0 4-6 10-6 10S0 10 0 6a6 6 0 0 1 6-6z" fill="#333"/><circle cx="6" cy="6" r="2" fill="#fff"/></svg><div>Funeral Home Korvelaer<br>Lindeweg 14, 3770 Zussen (Riemst)</div></div>
  <div class="row"><svg width="10" height="10" viewBox="0 0 24 24"><path d="M5 3l4 1 1 5-2 2c1 3 3 5 6 6l2-2 5 1 1 4-3 2C10 22 2 14 3 6z" fill="#333"/></svg><div>012 34 56 78</div></div>
  <div class="row"><svg width="10" height="10" viewBox="0 0 20 20"><rect x="2" y="7" width="16" height="8" fill="#333"/><rect x="5" y="2" width="10" height="5" fill="none" stroke="#333" stroke-width="2"/><rect x="5" y="13" width="10" height="5" fill="#fff" stroke="#333" stroke-width="2"/></svg><div>012 34 56 78</div></div>
  <div class="row"><svg width="12" height="10" viewBox="0 0 24 20" fill="none" stroke="#333" stroke-width="2"><path d="M2 8l10-6 10 6v11H2z M2 8l10 7 10-7"/></svg><div style="font-size:9px">mourningcenter.korvelaer@example.com</div></div>
</div>

<div class="minimap" role="img" aria-label="Small regional map around Riemst with a location marker"></div>

<div class="f-brand"><span class="dot"></span><span class="name">Funeral home<br>Korvelaer bvba</span></div>
<div class="social">
  <span style="background:#3b5998"></span><span style="background:#1da1f2"></span><span style="background:#0e76a8"></span><span style="background:#a9775a"></span>
</div>

<footer class="bottom">
  <div class="copy">Copyright © 2019 Funeral Home Korvelaer. All Rights Reserved.</div>
  <div class="legal">Sitemap &nbsp; I &nbsp; Privacy Policy</div>
</footer>
</body>
</html>
```